New Signage Design Project

Real estate company looking for signage, PowerPoint and stationery branding. Signs will be placed in front of homes and other properties being sold

Name of company is Birch Crest, LLC

Requirements
Must have
• Name of company - Birch Crest, LLC

```html
<!DOCTYPE html>
<html lang="en">
<head>
<meta charset="utf-8">
<title>Birch Crest, LLC – Sold Sign</title>
<link href="https://fonts.googleapis.com/css2?family=Montserrat:wght@800&display=swap" rel="stylesheet">
<style>
  :root {
    --page: #ffffff;
    --charcoal: #232c2c;
    --white: #ffffff;
    --sage: #82a09c;
    --coral: #e04e5c;
    --shadow: rgba(0, 0, 0, 0.25);
  }
  html, body {
    margin: 0;
    padding: 0;
    width: 1200px;
    height: 731px;
    overflow: hidden;
    background: var(--page);
  }
  .sold-sign {
    position: absolute;
    left: 180px;
    top: 51px;
    width: 840px;
    height: 629px;
    background: var(--charcoal);
    box-shadow: 0 2px 6px var(--shadow);
    overflow: hidden;
  }
  .sign-graphics {
    position: absolute;
    inset: 0;
    width: 100%;
    height: 100%;
  }
  .sold-headline {
    position: absolute;
    left: 58px;
    top: 72px;
    height: 190px;
    margin: 0;
    display: flex;
    align-items: center;
    font-family: "Montserrat", sans-serif;
    font-weight: 800;
    font-size: 212px;
    line-height: 1;
    letter-spacing: -4px;
    color: var(--charcoal);
  }
  .brand-block {
    position: absolute;
    left: 70px;
    top: 405px;
    display: flex;
    align-items: center;
    gap: 20px;
  }
  .brand-dot {
    width: 58px;
    height: 58px;
    border-radius: 50%;
    background: var(--coral);
  }
  .brand-name {
    font-family: "Montserrat", sans-serif;
    font-weight: 800;
    font-size: 40px;
    color: var(--white);
    white-space: nowrap;
  }
</style>
</head>
<body>
  <div class="sold-sign">
    <svg class="sign-graphics" viewBox="0 0 505 378" preserveAspectRatio="none" aria-hidden="true">
      <defs>
        <linearGradient id="fadeStripe" x1="0" y1="0" x2="0" y2="1">
          <stop offset="0" stop-color="#ffffff"/>
          <stop offset="1" stop-color="#232c2c" stop-opacity="0"/>
        </linearGradient>
      </defs>
      <polygon class="headline-band" points="0,43 500,43 407,157 0,157" fill="var(--white)"/>
      <polygon class="stripe-sage" points="505,46 505,74 421,176 394,176" fill="var(--sage)"/>
      <polygon class="stripe-coral" points="505,100 505,128 400,251 378,251" fill="var(--coral)"/>
      <polygon class="stripe-fade" points="464,206 502,206 354,378 334,378" fill="url(#fadeStripe)"/>
    </svg>
    <h1 class="sold-headline">SOLD</h1>
    <div class="brand-block">
      <span class="brand-dot"></span>
      <span class="brand-name">Birch Crest, LLC</span>
    </div>
  </div>
</body>
</html>
```